Pet sitting and Dog Walking Postcard distributed to new home owners in our target market

We need a two-sided postcard (or rack card, size can be anything rack card size or smaller) that is going in a folder that will be distributed each month to new homeowners in our target area. I would like the design to be similar to our brochure which will be uploaded here for you to see. It needs much less information than the brochure.
Should include services we offer; and our 4 systems: online registration, complimentary consultation, flexible scheduling, visits with reports and photos. Should also include our contact information (website, email, phone). Photos from the brochure can be used. Tagline from the cover of the brochure can be used. Call to action should be: Register on our website today to receive a free consultation and $20 off your first booking (when requesting a service, mention the promo code: welcome20).

```html
<!DOCTYPE html>
<html lang="en">
<head>
<meta charset="utf-8">
<title>Hound Haven Pet Care – Rack Card</title>
<link rel="stylesheet" href="https://fonts.googleapis.com/css2?family=Bebas+Neue&family=Montserrat:wght@400;500;600;700;800;900&display=swap">
<style>
  :root {
    --purple: #5a3c5e;
    --green: #43a035;
    --ink: #151515;
    --white: #ffffff;
    --stage: #9b9b9b;
  }
  * { box-sizing: border-box; margin: 0; padding: 0; }
  html, body { width: 1200px; height: 1200px; overflow: hidden; }
  body { background: var(--stage); font-family: "Montserrat", sans-serif; position: relative; }

  .card { position: absolute; top: 50px; width: 475px; height: 1100px; overflow: hidden; background: var(--purple); }
  .card--front { left: 85px; }
  .card--back { left: 648px; }
  .abs { position: absolute; }
  .center { left: 0; right: 0; text-align: center; white-space: nowrap; }

  /* front */
  .hero-photo { left: 0; top: 0; width: 475px; height: 700px;
    background: linear-gradient(160deg, #e9ece4 0%, #d8dccf 30%, #5f7a3a 60%, #2f4a1c 100%); }
  .arch { left: 0; top: 0; width: 475px; height: 1100px; }
  .brand-badge { left: 113px; top: 452px; width: 248px; height: 248px; border-radius: 50%;
    background: var(--white); border: 5px solid var(--green);
    display: flex; align-items: center; justify-content: center; }
  .brand-name { font-weight: 800; font-size: 30px; line-height: 1.1; color: var(--purple); text-align: center; text-transform: uppercase; }
  .tagline-lead { top: 728px; font-family: "Bebas Neue", sans-serif; font-size: 61px; font-weight: 400; color: var(--white); line-height: 1; }
  .tagline-focus { top: 790px; font-weight: 900; font-size: 45px; line-height: 1.05; color: var(--green); }
  .rule { left: 193px; top: 896px; width: 96px; height: 4px; background: var(--green); }
  .services { top: 917px; font-weight: 500; font-size: 20.5px; letter-spacing: 1px; color: var(--white); }

  .contact { left: 0; top: 967px; width: 475px; height: 121px; }
  .contact--light { background: var(--white); }
  .contact--dark { background: var(--purple); }
  .contact-phone { position: absolute; left: 0; right: 0; top: 18px; display: flex; align-items: center; justify-content: center; gap: 14px;
    font-weight: 800; font-size: 38px; }
  .contact--light .contact-phone { color: var(--ink); }
  .contact--dark .contact-phone { color: var(--white); }
  .phone-icon { width: 58px; height: 58px; }
  .contact-web { position: absolute; left: 0; right: 0; top: 90px; text-align: center; font-size: 14.5px; white-space: nowrap; }
  .contact--light .contact-web { color: var(--ink); }
  .contact--dark .contact-web { color: var(--white); }
  .dot { display: inline-block; width: 6px; height: 6px; border-radius: 50%; background: var(--green); margin: 0 8px; vertical-align: middle; }
  .base-bar { left: 0; top: 1088px; width: 475px; height: 12px; background: var(--green); }

  /* back */
  .back-title { top: 28px; font-family: "Bebas Neue", sans-serif; font-size: 44px; font-weight: 400; color: var(--green); line-height: 1; }
  .intro { left: 44px; width: 389px; top: 74px; font-size: 13.5px; line-height: 17.5px; color: var(--white); text-align: justify; letter-spacing: .3px; }
  .system { left: 48px; width: 420px; height: 80px; display: flex; align-items: center; }
  .system-icon { width: 68px; height: 68px; border-radius: 50%; background: var(--green); flex: none; display: flex; align-items: center; justify-content: center; }
  .system-label { margin-left: 36px; font-weight: 700; font-size: 15px; color: var(--white); white-space: nowrap; }
  .divider { left: 40px; width: 395px; border-top: 2px dotted var(--green); }
  .lower { left: 0; top: 0; width: 475px; height: 1100px; }
  .snap { border-radius: 50%; border: 4px solid var(--green); }
  .register { top: 697px; font-weight: 700; font-size: 14px; color: var(--ink); }
  .free { top: 714px; font-weight: 700; font-size: 33px; line-height: 1.2; color: var(--purple); }
  .offer { top: 751px; font-family: "Bebas Neue", sans-serif; font-weight: 400; font-size: 152px; line-height: 1; color: var(--green); }
  .first { top: 880px; font-weight: 700; font-size: 17px; line-height: 1.2; letter-spacing: 1px; color: var(--purple); }
  .promo { left: 52px; width: 367px; top: 912px; height: 36px; border: 2px dashed var(--ink); display: flex; align-items: center; justify-content: center;
    font-weight: 600; font-size: 20px; letter-spacing: 1.5px; color: var(--green); white-space: nowrap; }
</style>
</head>
<body>

<!-- Front -->
<section class="card card--front">
  <div class="abs hero-photo" role="img" aria-label="Photo of a spotted dog wearing a bow tie sitting in tall grass beside a bride and groom holding hands"></div>
  <svg class="abs arch" viewBox="0 0 475 1100">
    <path d="M0 636 Q237 470 475 636 L475 1100 L0 1100 Z" fill="var(--purple)"/>
    <path d="M0 636 Q237 470 475 636" fill="none" stroke="var(--green)" stroke-width="6"/>
  </svg>
  <div class="abs brand-badge"><div class="brand-name">Hound Haven<br>Pet Care</div></div>

  <h1 class="abs center tagline-lead">PRIORITIZE YOURSELF</h1>
  <h2 class="abs center tagline-focus">WE’LL FOCUS ON<br>YOUR PETS</h2>
  <div class="abs rule"></div>
  <p class="abs center services">PROFESSIONAL PET CARE SERVICES</p>

  <div class="abs contact contact--light">
    <div class="contact-phone">
      <svg class="phone-icon" viewBox="0 0 58 58"><circle cx="29" cy="29" r="27" fill="none" stroke="var(--green)" stroke-width="2.5"/><path d="M23 16 l5 0 l1 8 l-4 2 q1 7 6 12 l3-3 l6 3 l-1 5 q-10 1 -15-9 q-5-9 -1-18 z" fill="var(--green)"/></svg>
      <span>555-014-WOOF</span>
    </div>
    <p class="contact-web">www.houndhavenpets.com<span class="dot"></span>info@houndhavenpets.com</p>
  </div>
  <div class="abs base-bar"></div>
</section>

<!-- Back -->
<section class="card card--back">
  <h2 class="abs center back-title">READY TO FREE UP YOUR TIME?</h2>
  <p class="abs intro">We are here to uncomplicate your life! Our systems and processes allow for seamless scheduling, service and billing. Give us a few minutes of your time and we will deliver it back to you tenfold!</p>

  <div class="abs system" style="top:156px">
    <div class="system-icon"><svg width="38" height="38" viewBox="0 0 38 38" fill="none" stroke="#fff" stroke-width="2"><rect x="3" y="5" width="32" height="22" rx="2"/><path d="M15 27v5M23 27v5M11 33h16M8 10h10v12H8zM21 10h9M21 14h9M21 18h9"/></svg></div>
    <span class="system-label">ONLINE REGISTRATION</span>
  </div>
  <div class="abs divider" style="top:242px"></div>
  <div class="abs system" style="top:250px">
    <div class="system-icon"><svg width="38" height="38" viewBox="0 0 38 38" fill="none" stroke="#fff" stroke-width="2"><rect x="3" y="5" width="22" height="15" rx="2"/><rect x="14" y="15" width="21" height="14" rx="2" fill="#fff"/><path d="M7 10h14M7 14h8"/><path d="M18 20h13M18 24h13" stroke="var(--green)"/><path d="M28 29v4l-4-4"/></svg></div>
    <span class="system-label" style="margin-left:32px">COMPLIMENTARY CONSULTATION</span>
  </div>
  <div class="abs divider" style="top:334px"></div>
  <div class="abs system" style="top:342px">
    <div class="system-icon"><svg width="38" height="38" viewBox="0 0 38 38" fill="none" stroke="#fff" stroke-width="2"><rect x="4" y="7" width="30" height="27" rx="3"/><path d="M4 14h30M12 3v8M26 3v8"/><path d="M10 19h4v4h-4zM17 19h4v4h-4zM24 19h4v4h-4zM10 26h4v4h-4zM17 26h4v4h-4zM24 26h4v4h-4z"/></svg></div>
    <span class="system-label">FLEXIBLE SCHEDULING</span>
  </div>
  <div class="abs divider" style="top:425px"></div>
  <div class="abs system" style="top:430px">
    <div class="system-icon"><svg width="38" height="38" viewBox="0 0 38 38" fill="none" stroke="#fff" stroke-width="2"><rect x="6" y="4" width="24" height="20" rx="2"/><path d="M9 20l6-7 5 5 3-3 4 5"/><rect x="3" y="20" width="19" height="14" rx="2" fill="#fff"/><circle cx="12.5" cy="27" r="3.5" stroke="var(--green)"/><path d="M30 10l5 3-6 17"/></svg></div>
    <span class="system-label">VISITS WITH REPORTS AND PHOTOS</span>
  </div>

  <svg class="abs lower" viewBox="0 0 475 1100">
    <path d="M0 668 Q237 560 475 668 L475 967 L0 967 Z" fill="var(--white)"/>
    <path d="M0 668 Q237 560 475 668" fill="none" stroke="var(--green)" stroke-width="6"/>
  </svg>
  <div class="abs snap" style="left:42px;top:530px;width:136px;height:136px;background:radial-gradient(circle at 55% 45%, #f3e2c3, #d9a35a 60%, #a5642a)" role="img" aria-label="Photo of a yellow labrador holding a blue leash in its mouth"></div>
  <div class="abs snap" style="left:290px;top:532px;width:130px;height:130px;background:radial-gradient(circle at 50% 55%, #a07a62, #6b4a3a 55%, #d8d2cc)" role="img" aria-label="Photo of a woman cuddling a brown and white puppy"></div>
  <div class="abs snap" style="left:158px;top:504px;width:164px;height:164px;background:radial-gradient(circle at 45% 55%, #b9aca0, #8e8177 55%, #e3dbd2)" role="img" aria-label="Photo of a tabby cat being petted by a hand"></div>

  <p class="abs center register">REGISTER ON OUR WEBSITE TODAY TO RECEIVE A</p>
  <p class="abs center free">FREE CONSULTATION</p>
  <p class="abs center offer">$20 OFF</p>
  <p class="abs center first">YOUR FIRST BOOKING</p>
  <div class="abs promo">PROMO CODE: WELCOME20</div>

  <div class="abs contact contact--dark">
    <div class="contact-phone">
      <svg class="phone-icon" viewBox="0 0 58 58"><circle cx="29" cy="29" r="27" fill="none" stroke="var(--white)" stroke-width="2.5"/><path d="M23 16 l5 0 l1 8 l-4 2 q1 7 6 12 l3-3 l6 3 l-1 5 q-10 1 -15-9 q-5-9 -1-18 z" fill="var(--green)"/></svg>
      <span>555-014-WOOF</span>
    </div>
    <p class="contact-web">www.houndhavenpets.com<span class="dot"></span>info@houndhavenpets.com</p>
  </div>
  <div class="abs base-bar"></div>
</section>

</body>
</html>
```